Business Card Design

Copperfield Lantern & Spark, Inc. (CLS), located in Memphis, TN began operating on 2003. We are a certified
minority woman-owned business that genuinely takes a vested interest in our customers. We serve utilities,
government, contractors and end user markets in electrical, water, gas and industrial supplies. Our core
competency as a distributor of electrical materials has positioned us to serve business of all size. As your supply
chain partner, we arm you with the resources you need to make your supply chain more efficient. Our team
works with your team on a daily basis to help you solve problems and achieve goals. This team approach has
helped CLS customers to succeed and we can do the same for you.

NAICS Codes:
423610 Electrical Apparatus and Equipment, Wiring Supplies, and Related Equipment Merchant
Wholesalers
423510 Metal Service Centers and Other Metal Merchant Wholesalers
423720 Plumbing and Heating Equipment and Supplies (Hydronics) Merchant Wholesalers

Certifications
MBE (KRVPQAL, State of Tennessee Up-MRX and FJW), WBE (HQOLT),
WOSB, DOT (TDOT, MDOT, ALDOT, SCDOT, NCDOT, and VDOT), LOSB,
SBE, and LSB Certified
Some of Our Products Include:
. Boxes & Covers
. Conduit & Raceway
. Fittings
. Fuses
. Lamp & Ballasts
. Lighting Controls & Timers
. Lighting Fixtures
. Personal Safety
. Pipes
. Power Distribution
. Terminations Ground & Splices
. Tools & Testers
. Wire, Cords & Cable
. Wiring Devices
. Valves

Industry/Entity Type

Business

Contact Information for Business Card

Marianne T. Holloway - President/CEO
4728 Quillon Ave., Memphis, TN 38127
901-555-0147 office, 901-555-0182 fax, 901-555-0163 cell
mtholloway@clsllc-example.com - www.clsincorp-example.com

```html
<!DOCTYPE html>
<html lang="en">
<head>
<meta charset="utf-8">
<title>Copperfield Lantern &amp; Spark, Inc. — Business Card</title>
<link rel="stylesheet" href="https://fonts.googleapis.com/css2?family=Cinzel:wght@400;600&family=Tinos&family=PT+Sans:ital,wght@0,700;1,400&display=swap">
<style>
  :root {
    --backdrop: #a3a3a3;
    --card-light: #f1f1f1;
    --ink: #1a1a1a;
    --ink-soft: #4a4a4a;
    --olive: #8f9b1c;
    --black: #050505;
    --white: #ffffff;
    --rule: #b9b9b9;
  }
  * { margin: 0; padding: 0; box-sizing: border-box; }
  html, body { width: 1105px; height: 1200px; overflow: hidden; background: var(--backdrop); }
  .canvas { position: relative; width: 1105px; height: 1200px; }

  .card { position: absolute; left: 182px; width: 746px; height: 427px; overflow: hidden; }
  .card--front { top: 119px; background: var(--card-light); }
  .card--back { top: 637px; background: var(--black); }

  /* front */
  .brand-name {
    position: absolute; left: 30px; top: 168px; width: 330px;
    font-family: "Tinos", serif; font-size: 30px; line-height: 1.12;
    color: var(--black); text-transform: uppercase; letter-spacing: 0.5px;
  }
  .brand-mark { position: absolute; left: 30px; top: 136px; width: 20px; height: 20px; border-radius: 50%; background: var(--olive); }
  .divider { position: absolute; left: 374px; top: 77px; width: 1px; height: 280px; background: var(--rule); }
  .contact { position: absolute; left: 402px; top: 76px; }
  .contact__name { font-family: "Cinzel", serif; font-weight: 600; font-size: 25px; color: var(--ink); letter-spacing: 0.6px; line-height: 32px; }
  .contact__title { font-family: "Cinzel", serif; font-size: 22px; color: var(--olive); line-height: 30px; }
  .contact__address { margin-top: 6px; font-family: "Tinos", serif; font-size: 21.5px; color: var(--ink-soft); line-height: 26px; }
  .contact__list { list-style: none; margin-top: 8px; font-family: "Tinos", serif; font-size: 20.5px; color: var(--ink-soft); }
  .contact__list li { display: flex; align-items: center; height: 29px; }
  .contact__list svg { width: 18px; height: 18px; margin-right: 10px; fill: var(--ink); flex: none; }
  .accent-line { position: absolute; left: 0; bottom: 32px; width: 100%; height: 3px; background: var(--olive); }
  .footer-band { position: absolute; left: 0; bottom: 0; width: 100%; height: 32px; background: var(--black); }

  /* back */
  .back-brand { position: absolute; left: 0; top: 120px; width: 100%; text-align: center; }
  .back-brand__mark { display: inline-block; width: 22px; height: 22px; border-radius: 50%; background: var(--olive); vertical-align: middle; margin-right: 12px; }
  .back-brand__name { font-family: "Tinos", serif; font-size: 34px; color: var(--white); text-transform: uppercase; letter-spacing: 1px; vertical-align: middle; }
  .back-rule { position: absolute; left: 142px; top: 239px; width: 462px; height: 1px; background: linear-gradient(90deg, transparent, #5a5a5a 30%, #5a5a5a 70%, transparent); }
  .products { position: absolute; left: 0; top: 260px; width: 100%; text-align: center; font-family: "PT Sans", sans-serif; color: var(--white); }
  .products__heading { font-weight: 700; font-size: 19px; color: var(--olive); line-height: 26px; }
  .products__line { font-style: italic; font-size: 18px; line-height: 23px; }
</style>
</head>
<body>
<main class="canvas">
  <section class="card card--front">
    <span class="brand-mark"></span>
    <div class="brand-name">Copperfield Lantern<br>&amp; Spark, Inc.</div>
    <div class="divider"></div>
    <div class="contact">
      <p class="contact__name">Marianne T. Holloway</p>
      <p class="contact__title">President/CEO</p>
      <p class="contact__address">4728 Quillon Ave.<br>Memphis, TN 38127</p>
      <ul class="contact__list">
        <li><svg viewBox="0 0 24 24"><path d="M6.6 10.8a15.2 15.2 0 0 0 6.6 6.6l2.2-2.2c.3-.3.7-.4 1-.2 1.1.4 2.3.6 3.6.6.6 0 1 .4 1 1V20c0 .6-.4 1-1 1A17 17 0 0 1 3 4c0-.6.4-1 1-1h3.5c.6 0 1 .4 1 1 0 1.3.2 2.5.6 3.6.1.3 0 .7-.2 1z"/></svg>901-555-0147</li>
        <li><svg viewBox="0 0 24 24"><path d="M7 1h10a2 2 0 0 1 2 2v18a2 2 0 0 1-2 2H7a2 2 0 0 1-2-2V3a2 2 0 0 1 2-2zm0 3v14h10V4z"/></svg>901-555-0182</li>
        <li><svg viewBox="0 0 24 24"><path d="M6 2h12v5H6zM3 8h18a2 2 0 0 1 2 2v7h-4v5H5v-5H1v-7a2 2 0 0 1 2-2zm4 7v5h10v-5z"/></svg>901-555-0163</li>
        <li><svg viewBox="0 0 24 24"><path d="M2 5h20v14H2zm2 2v.5l8 5 8-5V7l-8 5z"/></svg>mtholloway@clsllc-example.com</li>
        <li><svg viewBox="0 0 24 24"><path d="M12 2a10 10 0 1 0 0 20 10 10 0 0 0 0-20zm-1 17.9A8 8 0 0 1 4.2 10L9 14.8v1c0 1.1.9 2 2 2zm6.9-2.5A2 2 0 0 0 16 16h-1v-3a1 1 0 0 0-1-1H8v-2h2a1 1 0 0 0 1-1V7h2a2 2 0 0 0 2-2v-.4a8 8 0 0 1 2.9 12.8z"/></svg>www.clsincorp-example.com</li>
      </ul>
    </div>
    <div class="accent-line"></div>
    <div class="footer-band"></div>
  </section>

  <section class="card card--back">
    <div class="back-brand"><span class="back-brand__mark"></span><span class="back-brand__name">Copperfield Lantern &amp; Spark</span></div>
    <div class="back-rule"></div>
    <div class="products">
      <p class="products__heading">Some of Our Products Include:</p>
      <p class="products__line">Boxes &amp; Covers | Conduit &amp; Raceway | Fittings</p>
      <p class="products__line">Fuses | Lamp &amp; Ballasts | Lighting Controls &amp; Timers | Lighting Fixtures</p>
      <p class="products__line">Personal Safety | Pipes | Power Distribution | Terminations Ground &amp; Splices</p>
      <p class="products__line">Tools &amp; Testers | Wire, Cords &amp; Cable | Wiring Devices | Valves</p>
    </div>
  </section>
</main>
</body>
</html>
```